Chicken Coop Sign

I would like to make a metal chicken coop sign in the size of 8 x 12 inches. The orientation can be vertical or horizontal.

I would like the designer to use any of these funny phrases and try and create a catchy graphic based on some of the designs that are already in the market.

"The Poultry Palace: Where Every Hen is a Queen"

"The Hen Den: No Foxes Allowed"

"The Eggsecutive Mansion"

"The Cluck Hut: No Fowl Moods Allowed"

"The Cluck and Fluff: Luxury Lodging for Hens"

Target Market(s)

Families that have chicken coops as a hobby in their backyard or farm.

Requirements
Must have
• It must be funny, use one of the provided quotes, have a "vintage" or "rustic" look
Nice to have
Should not have
• Stay away from 4 letter words like "SHIT", "FUCK" or Starred out works like "S**T" and "F**K"

```html
<!DOCTYPE html>
<html lang="en">
<head>
<meta charset="utf-8">
<title>The Hen Den – No Foxes Allowed</title>
<link rel="stylesheet" href="https://fonts.googleapis.com/css2?family=Black+Ops+One&display=swap">
<style>
  :root {
    --sign-red: #ea1c2a;
    --sign-white: #ffffff;
    --ink-black: #0b0b0b;
    --fox-orange: #e8892c;
    --fox-light: #f6c48a;
    --fox-dark: #b4561a;
  }
  html, body {
    margin: 0;
    padding: 0;
    width: 800px;
    height: 1200px;
    overflow: hidden;
    background: var(--sign-white);
  }
  .sign {
    display: block;
    width: 800px;
    height: 1200px;
  }
  .sign-text {
    font-family: "Black Ops One", "Arial Black", sans-serif;
  }
  .title-text { fill: var(--ink-black); }
  .warning-text { fill: var(--sign-red); }
  .sign-frame { fill: var(--sign-red); }
  .sign-panel { fill: var(--sign-white); }
  .hen-silhouette { fill: var(--ink-black); }
  .prohibition-ring,
  .prohibition-slash {
    fill: none;
    stroke: var(--sign-red);
    stroke-width: 24;
  }
</style>
</head>
<body>
<svg class="sign" viewBox="0 0 800 1200" xmlns="http://www.w3.org/2000/svg">
  <defs>
    <radialGradient id="fox-tones" cx="50%" cy="55%" r="60%">
      <stop offset="0%" stop-color="var(--fox-light)"/>
      <stop offset="60%" stop-color="var(--fox-orange)"/>
      <stop offset="100%" stop-color="var(--fox-dark)"/>
    </radialGradient>
  </defs>

  <!-- Frame and panel -->
  <rect class="sign-frame" x="0" y="0" width="800" height="1200"/>
  <rect class="sign-panel" x="27" y="27" width="746" height="1146"/>

  <!-- Hen silhouettes -->
  <rect class="hen-silhouette" x="150" y="53" width="97" height="164" rx="30"
        role="img" aria-label="Black silhouette of a hen facing right"/>
  <rect class="hen-silhouette" x="553" y="53" width="97" height="164" rx="30"
        role="img" aria-label="Black silhouette of a hen facing left"/>

  <!-- Title -->
  <text class="sign-text title-text" x="400" y="203" text-anchor="middle"
        font-size="150" textLength="220" lengthAdjust="spacingAndGlyphs">THE</text>
  <text class="sign-text title-text" x="402" y="357" text-anchor="middle"
        font-size="150" textLength="550" lengthAdjust="spacingAndGlyphs">HEN DEN</text>

  <!-- Fox with prohibition sign -->
  <rect x="193" y="420" width="420" height="427" rx="90" fill="url(#fox-tones)"
        role="img" aria-label="Illustrated red fox head looking forward"/>
  <circle class="prohibition-ring" cx="407" cy="623" r="225"/>
  <line class="prohibition-slash" x1="566" y1="464" x2="248" y2="782"/>

  <!-- Warning -->
  <text class="sign-text warning-text" x="400" y="1007" text-anchor="middle"
        font-size="150" textLength="600" lengthAdjust="spacingAndGlyphs">NO FOXES</text>
  <text class="sign-text warning-text" x="400" y="1150" text-anchor="middle"
        font-size="150" textLength="566" lengthAdjust="spacingAndGlyphs">ALLOWED</text>
</svg>
</body>
</html>
```